Bluestone Health Clinic needs a newspaper ad design

We need a newspaper ad for our Health Clinic. We provide primary medical care, medicated addiction therapy, psychiatric care, and psychotherapy in person and would really like to promote our teletherapy. So I have attached our company logo as well.

```html
<!DOCTYPE html>
<html lang="en">
<head>
<meta charset="utf-8">
<title>Larkmoor Medical &amp; Associates – Newspaper Ad</title>
<link rel="stylesheet" href="https://fonts.googleapis.com/css2?family=Kalam:wght@400&family=Roboto:wght@700&display=swap">
<style>
  :root {
    --paper: #ffffff;
    --page-bg: #e9e6e1;
    --red: #ec1c24;
    --blue: #3a4fa3;
    --green-dark: #0f3d1f;
    --green-mid: #2e7a43;
    --ink: #1a1a1a;
    --white: #ffffff;
    --ring: #111111;
  }
  html, body {
    margin: 0;
    padding: 0;
    overflow: hidden;
    background: var(--page-bg);
  }
  .ad {
    position: relative;
    width: 1200px;
    height: 795px;
    background: var(--paper);
    overflow: hidden;
  }
  .ad__shapes {
    position: absolute;
    inset: 0;
  }
  .brand {
    position: absolute;
    left: 200px;
    top: 52px;
    display: flex;
    align-items: center;
    gap: 16px;
    font-family: "Kalam", cursive;
    color: var(--ink);
  }
  .brand__mark {
    width: 58px;
    height: 58px;
    background: var(--red);
    flex: none;
  }
  .brand__name {
    font-size: 46px;
    line-height: 1;
    margin: 0;
    font-weight: 400;
  }
  .brand__tagline {
    margin: 4px 0 0;
    font-size: 26px;
    line-height: 1;
  }
  .services {
    position: absolute;
    left: 70px;
    top: 262px;
    margin: 0;
    padding: 0;
    list-style: none;
    font-family: "Roboto", sans-serif;
    font-weight: 700;
    font-size: 40px;
    line-height: 1.12;
    color: var(--white);
    white-space: nowrap;
  }
  .services__item {
    display: flex;
    gap: 14px;
    align-items: flex-start;
    margin-bottom: 6px;
  }
  .services__tick {
    flex: none;
    width: 30px;
    height: 30px;
    margin-top: 8px;
  }
  .photo {
    position: absolute;
    border-radius: 50%;
    border: 5px solid var(--ring);
    box-sizing: border-box;
  }
  .photo--desk {
    left: 560px;
    top: 235px;
    width: 300px;
    height: 300px;
    background: radial-gradient(circle at 55% 45%, #d9d4cc, #8f8a86 70%, #4a4744);
  }
  .photo--session {
    left: 360px;
    top: 520px;
    width: 270px;
    height: 270px;
    background: radial-gradient(circle at 50% 50%, #a55a2a, #6b3216 70%, #3a1a0b);
  }
</style>
</head>
<body>
<main class="ad">
  <svg class="ad__shapes" width="1200" height="795" viewBox="0 0 1200 795" aria-hidden="true">
    <path d="M0 215 C150 170 300 175 430 232 C530 285 580 385 605 480 L640 795 L0 795 Z" fill="var(--red)"/>
    <path d="M610 795 C640 560 760 360 960 260 C1060 215 1140 200 1200 198 L1200 795 Z" fill="var(--blue)"/>
  </svg>
  <svg class="ad__shapes" width="1200" height="795" viewBox="0 0 1200 795" role="img" aria-label="Silhouette of a head blended with a calm lake landscape in green tones">
    <defs>
      <linearGradient id="greenScene" x1="0" y1="0" x2="0" y2="1">
        <stop offset="0" stop-color="var(--green-mid)"/>
        <stop offset="1" stop-color="var(--green-dark)"/>
      </linearGradient>
    </defs>
    <path d="M640 795 C670 580 790 390 985 295 C1080 250 1150 232 1200 228 L1200 795 Z" fill="url(#greenScene)"/>
  </svg>

  <header class="brand">
    <span class="brand__mark"></span>
    <div>
      <h1 class="brand__name">Larkmoor Medical &amp; Associates, LLC</h1>
      <p class="brand__tagline">Dedicated to Hope, Healing &amp; Recovery</p>
    </div>
  </header>

  <ul class="services">
    <li class="services__item">
      <svg class="services__tick" viewBox="0 0 30 30"><rect x="2" y="6" width="22" height="22" fill="none" stroke="#fff" stroke-width="3"/><path d="M7 16 L13 22 L28 4" fill="none" stroke="#fff" stroke-width="4"/></svg>
      <span>Medicated<br>addiction therapy</span>
    </li>
    <li class="services__item">
      <svg class="services__tick" viewBox="0 0 30 30"><rect x="2" y="6" width="22" height="22" fill="none" stroke="#fff" stroke-width="3"/><path d="M7 16 L13 22 L28 4" fill="none" stroke="#fff" stroke-width="4"/></svg>
      <span>Psychiatric care</span>
    </li>
    <li class="services__item">
      <svg class="services__tick" viewBox="0 0 30 30"><rect x="2" y="6" width="22" height="22" fill="none" stroke="#fff" stroke-width="3"/><path d="M7 16 L13 22 L28 4" fill="none" stroke="#fff" stroke-width="4"/></svg>
      <span>Psychotherapy in<br>person</span>
    </li>
    <li class="services__item">
      <svg class="services__tick" viewBox="0 0 30 30"><rect x="2" y="6" width="22" height="22" fill="none" stroke="#fff" stroke-width="3"/><path d="M7 16 L13 22 L28 4" fill="none" stroke="#fff" stroke-width="4"/></svg>
      <span>Teletherapy</span>
    </li>
  </ul>

  <div class="photo photo--desk" role="img" aria-label="Woman working thoughtfully at a laptop with a coffee mug"></div>
  <div class="photo photo--session" role="img" aria-label="Therapist taking notes while a client reclines on a couch in an office"></div>
</main>
</body>
</html>
```